Lawn care & general maintenance

I need a business card desisign for a new business in north bay called The Hedge Buddy i offer services like lawn care, snow removal, and general maintenance such as dry walling painting, brush removal, and other little maintenance work.

The font must be like the font on my work hate

Industry/Entity Type

Business

Contact Information for Business Card

Derek Ossington, Company name: The Hedge Buddy

Logo Text

The Hedge Buddy- in jetson print

Logo styles of interest
Pictorial/Combination Logo
Requirements
Must have
• Slogan: We trim back the hardest yards, just call!

```html
<!DOCTYPE html>
<html lang="en">
<head>
<meta charset="utf-8">
<title>The Hedge Buddy – Business Card</title>
<link rel="stylesheet" href="https://fonts.googleapis.com/css2?family=Arimo:wght@400;700&family=Carlito&display=swap">
<style>
  :root {
    --backdrop: #2b2b2d;
    --brand-red: #93353a;
    --accent-red: #c8313a;
    --paper: #ffffff;
    --lawn-green: #3f8c55;
    --hedge-tint: #e3f1e7;
    --title-green: #3f8c55;
    --ink-red: #93353a;
  }
  * { margin: 0; padding: 0; box-sizing: border-box; }
  html, body {
    width: 1200px;
    height: 1000px;
    overflow: hidden;
    background: var(--backdrop);
  }
  .canvas {
    position: relative;
    width: 1200px;
    height: 1000px;
  }
  .business-card {
    position: absolute;
    left: 380px;
    top: 140px;
    width: 440px;
    height: 720px;
    background: var(--paper);
    overflow: hidden;
    box-shadow: 0 12px 30px rgba(0,0,0,0.45);
  }
  .card-shapes {
    position: absolute;
    inset: 0;
    width: 100%;
    height: 100%;
  }
  .brand {
    position: absolute;
    left: 0;
    right: 0;
    top: 72px;
    text-align: center;
    color: var(--paper);
  }
  .brand-name {
    font-family: "Arimo", Arial, sans-serif;
    font-weight: 700;
    font-size: 32px;
    letter-spacing: 2px;
    text-transform: uppercase;
    line-height: 1;
  }
  .brand-slogan {
    font-family: "Carlito", Calibri, sans-serif;
    font-size: 15px;
    margin-top: 8px;
    letter-spacing: 0.2px;
  }
  .contact-block {
    position: absolute;
    left: 0;
    right: 0;
    top: 268px;
    text-align: center;
    font-family: "Arimo", Arial, sans-serif;
  }
  .person-name {
    color: var(--ink-red);
    font-weight: 700;
    font-size: 30px;
    line-height: 1.1;
  }
  .person-title {
    color: var(--title-green);
    font-size: 22px;
    margin-top: 2px;
  }
  .person-phone {
    color: var(--ink-red);
    font-size: 24px;
    margin-top: 44px;
  }
  .hedge-edge {
    position: absolute;
    inset: 0;
    width: 100%;
    height: 100%;
  }
  .services {
    position: absolute;
    left: 0;
    right: 0;
    top: 540px;
    text-align: center;
    color: var(--paper);
    font-family: "Carlito", Calibri, sans-serif;
    font-size: 24px;
    line-height: 1.18;
    list-style: none;
  }
</style>
</head>
<body>
<main class="canvas">
  <article class="business-card">
    <svg class="card-shapes" viewBox="0 0 440 720" aria-hidden="true">
      <path d="M0 0 H440 V150 Q380 148 300 158 Q150 180 0 222 Z" fill="var(--accent-red)"/>
      <path d="M0 0 H440 V128 Q370 126 290 138 Q140 160 0 205 Z" fill="var(--brand-red)"/>
      <path d="M0 462 L130 440 L260 432 L440 412 V720 H0 Z" fill="var(--lawn-green)"/>
      <path d="M0 456 L130 434 L260 426 L440 406" fill="none" stroke="var(--accent-red)" stroke-width="1.2"/>
    </svg>

    <svg class="hedge-edge" viewBox="0 0 440 720" role="img" aria-label="Line drawing of trees and bushes along the lawn edge">
      <path d="M0 456 L130 434 L260 426 L440 406 V380 L260 400 L130 408 L0 430 Z" fill="var(--hedge-tint)" opacity="0.6"/>
    </svg>

    <header class="brand">
      <div class="brand-name">The Hedge Buddy</div>
      <div class="brand-slogan">We trim back the hardest yards, just call!</div>
    </header>

    <section class="contact-block">
      <div class="person-name">Derek Ossington</div>
      <div class="person-title">Title</div>
      <div class="person-phone">Contact number</div>
    </section>

    <ul class="services">
      <li>Our Services :</li>
      <li>Lawn Care</li>
      <li>Snow removal</li>
      <li>Dry Walling Painting</li>
    </ul>
  </article>
</main>
</body>
</html>
```